Advertisement Coaching practice

I need an advertisement (to be printed in newspaper). I have a coaching practice where I offer coaching, workshops family constellations and relationship therapy. The ad needs to express calmness, inspiration to transform but also not dull and boring. It would be great if you could use the colors from my logo into the ad.

Dimensions are: 13,04 cm Width x 9,72 cm Height.

I will add my previous self-made ad, my company logo, a portrait photo of myself and the text I want to add. Also my contact details should be visible as well.

Requirements
Nice to have
• I have updated the brief with a flyer that I had previously made by a designer. It would be a nice to have if the ad ties in with that. You can also look at my website at www.bravemoor.nu to see what colors I used there.

```html
<!DOCTYPE html>
<html lang="nl">
<head>
<meta charset="utf-8">
<title>Advertentie coachingpraktijk</title>
<link rel="stylesheet" href="https://fonts.googleapis.com/css2?family=Montserrat:wght@600;800&family=Quicksand:wght@400;500;700&family=PT+Sans&display=swap">
<style>
  :root {
    --gold: #9a7d2c;
    --gold-light: #ad9040;
    --gold-dark: #836824;
    --navy: #1f3457;
    --white: #ffffff;
    --ink: #3c3c3c;
    --logo-grey: #5b5b5b;
    --backdrop: #c6c6c6;
  }
  * { margin: 0; padding: 0; box-sizing: border-box; }
  html, body { width: 1200px; height: 720px; overflow: hidden; background: var(--backdrop); }
  .ad {
    position: absolute; left: 130px; top: 9px; width: 940px; height: 702px; overflow: hidden;
    background: radial-gradient(ellipse at 60% 30%, var(--gold-light), var(--gold) 55%, var(--gold-dark));
    box-shadow: 0 2px 8px rgba(0,0,0,.12);
    font-family: "Quicksand", sans-serif;
  }
  .portrait {
    position: absolute; left: 0; top: 22px; width: 470px; height: 500px;
    background: radial-gradient(ellipse at 42% 40%, #b8876a 0%, #8d6a55 28%, #aab3c2 60%, rgba(170,180,195,0) 78%);
  }
  .waves { position: absolute; left: 0; top: 0; width: 940px; height: 702px; }
  .headline {
    position: absolute; right: 37px; top: 36px; text-align: right;
    font-family: "Montserrat", sans-serif; font-weight: 800; color: var(--white);
    font-size: 44px; line-height: 45px; letter-spacing: .3px;
  }
  .intro {
    position: absolute; left: 351px; top: 177px; width: 552px; height: 55px;
    background: var(--navy); border-radius: 28px;
    color: var(--white); font-size: 16px; line-height: 23px; text-align: right;
    padding: 4px 21px 0 0; letter-spacing: .2px;
  }
  .lead {
    position: absolute; right: 37px; top: 246px; color: var(--white);
    font-size: 18px; letter-spacing: .4px; font-weight: 400;
  }
  .lead strong { font-weight: 700; }
  .services { position: absolute; left: 455px; top: 283px; width: 460px; height: 130px; }
  .service { position: absolute; top: 0; width: 150px; text-align: center; }
  .service svg { width: 70px; height: 70px; display: block; margin: 0 auto; }
  .service p {
    margin-top: 9px; color: var(--white); font-family: "Montserrat", sans-serif;
    font-weight: 600; font-size: 11.5px; line-height: 15.5px;
  }
  .brand { position: absolute; left: 72px; top: 538px; width: 180px; text-align: center; }
  .brand-mark { width: 58px; height: 58px; border: 2px solid var(--logo-grey); border-radius: 50%; margin: 0 auto; }
  .brand-name { margin-top: 8px; font-family: "Quicksand", sans-serif; font-weight: 500; font-size: 34px; color: var(--logo-grey); }
  .about {
    position: absolute; right: 37px; top: 539px; width: 600px; text-align: right;
    color: var(--ink); font-size: 13.6px; line-height: 18.6px; font-weight: 500;
  }
  .contact {
    position: absolute; left: 299px; top: 638px; width: 641px; height: 25px;
    background: var(--gold); color: var(--white); font-size: 14px; font-weight: 500;
    display: flex; align-items: center; padding-left: 8px; white-space: nowrap;
  }
  .contact span { margin-right: 10px; }
</style>
</head>
<body>
  <div class="ad">
    <div class="portrait" role="img" aria-label="Portretfoto van de coach in een lichtblauwe blouse"></div>

    <svg class="waves" viewBox="0 0 940 702" aria-hidden="true">
      <path fill="var(--white)" d="M0,468 C120,506 260,512 430,486 C560,464 740,438 940,538 L940,702 L0,702 Z"/>
      <path fill="var(--navy)" d="M62,494 C200,516 330,498 452,468 C566,432 720,414 876,496 C720,456 570,470 436,500 C300,528 170,522 62,494 Z"/>
    </svg>

    <h1 class="headline">COACHING,<br>FAMILIEOPSTELLINGEN<br>&amp; RELATIETHERAPIE</h1>

    <p class="intro">Trauma’s en negatieve ervaringen vormen ons en blijven<br>nog lang voelbaar. Ze kunnen groei of geluk in de weg staan.</p>

    <p class="lead">IK BEN <strong>AMRITA</strong> EN ONDERSTEUN JE BIJ HET:</p>

    <div class="services">
      <div class="service" style="left:0">
        <svg viewBox="0 0 70 70"><circle cx="35" cy="35" r="33" fill="none" stroke="var(--navy)" stroke-width="3"/>
          <g fill="none" stroke="var(--white)" stroke-width="2">
            <circle cx="40" cy="28" r="13" fill="var(--white)" fill-opacity=".25"/>
            <ellipse cx="40" cy="28" rx="10" ry="4"/>
            <ellipse cx="40" cy="28" rx="10" ry="4" transform="rotate(60 40 28)"/>
            <ellipse cx="40" cy="28" rx="10" ry="4" transform="rotate(-60 40 28)"/>
            <path d="M18,50 C26,44 34,46 40,48 C46,49 52,45 56,42"/>
          </g>
          <rect x="11" y="45" width="5" height="10" fill="var(--white)"/>
        </svg>
        <p>Doorbreken van<br>belemmerende patronen</p>
      </div>
      <div class="service" style="left:151px">
        <svg viewBox="0 0 70 70"><circle cx="35" cy="35" r="33" fill="none" stroke="var(--navy)" stroke-width="3"/>
          <path fill="var(--white)" d="M12,30 L22,20 L34,26 L46,20 L58,30 L48,44 L40,52 L36,48 L32,52 L28,48 L24,50 L20,44 Z"/>
          <path fill="none" stroke="var(--navy)" stroke-width="1.5" d="M24,34 L34,26 M30,40 L38,34 M34,46 L42,40"/>
        </svg>
        <p>Beter omgaan met<br>conflicten</p>
      </div>
      <div class="service" style="left:300px">
        <svg viewBox="0 0 70 70"><circle cx="35" cy="35" r="33" fill="none" stroke="var(--navy)" stroke-width="3"/>
          <g stroke="var(--white)" stroke-width="1.5" fill="none">
            <polygon points="35,14 53,24 53,46 35,56 17,46 17,24" stroke-dasharray="3 2"/>
            <circle cx="35" cy="35" r="9" stroke-width="2.5"/>
          </g>
          <g fill="var(--white)">
            <circle cx="35" cy="14" r="3"/><circle cx="53" cy="24" r="3"/><circle cx="53" cy="46" r="3"/>
            <circle cx="35" cy="56" r="3"/><circle cx="17" cy="46" r="3"/><circle cx="17" cy="24" r="3"/>
            <rect x="33" y="29" width="4" height="12"/><rect x="29" y="33" width="12" height="4"/>
          </g>
        </svg>
        <p>In gezonde verbinding<br>met elkaar als koppel<br>of met anderen komen</p>
      </div>
    </div>

    <div class="brand">
      <div class="brand-mark"></div>
      <div class="brand-name">bravemoor</div>
    </div>

    <p class="about">Maandelijks geef ik workshops familieopstellingen. Ook houd ik themasessies rond adoptie, moeder-dochterdynamiek of relaties. Ook bied ik individuele coaching, relatietherapie en retraites aan. Kijk op de website voor meer info of neem contact open ontdek wat het beste bij jou past.</p>

    <div class="contact">
      <span>Amrita Veldkamp</span><span>| M: info@bravemoor.nu</span><span>| T: 06-41 27 93 58 |</span><span>www.bravemoor.nu</span>
    </div>
  </div>
</body>
</html>
```